Bright Lane Collective needs updated website.

Our current website was designed on wix.com. (www.brightlanecollective.example).
We would like something a little more customized for what our company offers. Bright Lane Collective is a company specializing in connecting consumers with trustworthy and affordable service professionals. We need the website to be approachable and easy to use, while conveying our "Bright Lane" reputation.
Reason: Our project is now guaranteed. Please send your ideas. Thank you!
Target Market(s)
Homeowners
Industry/Entity Type
It Company
Look and feel

```html
<!DOCTYPE html>
<html lang="en">
<head>
<meta charset="utf-8">
<title>Bright Lane Collective</title>
<link href="https://fonts.googleapis.com/css2?family=Oswald:wght@400;600;700&family=Cinzel:wght@400&family=Raleway:wght@300;400&family=Arimo:wght@400;700&display=swap" rel="stylesheet">
<style>
:root{
  --page:#f1f0f1;
  --navy:#0e3a66;
  --orange:#e0661a;
  --blue:#3f86c8;
  --ink:#1d1d1d;
  --text:#555;
  --concrete:#c9c7c5;
  --concrete-dark:#b3b0ad;
  --grid:rgba(255,255,255,.55);
}
*{margin:0;padding:0;box-sizing:border-box}
html,body{width:691px;height:1200px;overflow:hidden;background:var(--page)}
body{position:relative;font-family:"Raleway",sans-serif;color:var(--text)}
.abs{position:absolute}

/* hero */
.hero{position:absolute;left:0;top:0;width:691px;height:395px;overflow:hidden;
  background:linear-gradient(135deg,#d3d1cf,var(--concrete) 50%,var(--concrete-dark))}
.hero-portrait{position:absolute;left:0;top:0;width:345px;height:395px;
  background:linear-gradient(160deg,#8a7c70 0%,#4b4540 40%,#1e1e1f 75%,#121213 100%)}
.tile{position:absolute;width:115.2px;height:115.2px;border-right:1px solid var(--grid);border-bottom:1px solid var(--grid)}
.grid-lines{position:absolute;inset:0;pointer-events:none;
  background-image:linear-gradient(to right,var(--grid) 1px,transparent 1px),linear-gradient(to bottom,var(--grid) 1px,transparent 1px);
  background-size:115.2px 116px}
.tile-services{left:345.6px;top:0;background:#1f1f1f;color:#fff;font-family:"Oswald",sans-serif;text-align:center;padding-top:26px}
.tile-services .label{font-size:15px;font-weight:600;line-height:1;margin-left:-20px}
.tile-services .hours{font-size:29px;font-weight:600;line-height:1.05;margin-left:10px}
.tile-services .phone{font-size:11.5px;font-weight:600;letter-spacing:.2px}
.tile-phone-photo{left:460.8px;top:0;background:radial-gradient(circle at 50% 60%,#2a2f36 0 22%,#3f86c8 23%,#3a7fc1 100%)}
.tile-brand{left:230.4px;top:115.2px;background:rgba(240,239,238,.85);display:flex;align-items:center;justify-content:center;gap:5px}
.brand-dot{width:14px;height:14px;border-radius:50%;background:var(--blue);flex:none}
.brand-name{font-family:"Oswald",sans-serif;font-weight:600;font-size:11px;color:var(--navy);line-height:1.1}
.nav{position:absolute;top:115.2px;height:115.2px;width:115.2px;display:flex;align-items:center;justify-content:center;gap:7px;
  font-family:"Oswald",sans-serif;font-weight:600;font-size:13.5px;color:#111;text-decoration:none}
.nav svg{width:15px;height:15px;fill:#111}
.tile-painting{left:115.2px;top:230.4px;background:linear-gradient(160deg,#4d8fcf,#2f6fae);padding:36px 0 0 7px;font-family:"Oswald",sans-serif;color:rgba(255,255,255,.55);line-height:1}
.tile-painting .big{font-size:28px;font-weight:600}
.tile-painting .small{font-size:14px;font-weight:600}
.tile-car{left:345.6px;top:230.4px;background:linear-gradient(160deg,#9a9a9a,#3a3a3c 55%,#1c1c1d)}
.tile-tools{left:576px;top:230.4px;background:linear-gradient(135deg,#b9b5b0,#8b8681)}
.tile-paint{left:0;top:345.6px;height:50px;background:linear-gradient(90deg,#d6b536,#b5a48a 50%,#7a716a)}
.tile-auto{left:460.8px;top:348px;height:47px;background:var(--blue);color:rgba(255,255,255,.8);font-family:"Oswald",sans-serif;font-weight:600;font-size:14px;display:flex;align-items:flex-end;justify-content:center;padding-bottom:7px}
.hero-fade{position:absolute;left:0;right:0;bottom:0;height:10px;background:linear-gradient(transparent,rgba(0,0,0,.35))}

/* section heads */
.rule{position:absolute;height:1px;background:#3b4f66}
.section-title{position:absolute;font-family:"Oswald",sans-serif;font-weight:700;color:var(--navy);line-height:1}
.photo{position:absolute}
.bracket-tl,.bracket-br{position:absolute;width:19px;height:19px}
.bracket-tl{border-top:2px solid var(--navy);border-left:2px solid var(--navy)}
.bracket-br{border-bottom:2px solid var(--ink);border-right:2px solid var(--ink)}
.kicker{position:absolute;font-family:"Cinzel",serif;color:var(--orange);line-height:1}
.body-copy{position:absolute;font-size:7.3px;line-height:9.3px;color:#666;font-weight:400}
.read-more{position:absolute;font-family:"Cinzel",serif;font-size:6px;color:var(--navy);letter-spacing:.3px;text-decoration:none}

/* network */
.col-title{position:absolute;font-family:"Arimo",sans-serif;font-weight:700;font-size:13.5px;color:#111;line-height:1}
.service-list{position:absolute;list-style:none;font-size:8.6px;line-height:10px;color:#444}
.note{position:absolute;font-size:7.8px;line-height:9.6px;color:#444}
.note strong{font-weight:400;font-size:12px;color:var(--navy)}
.video{position:absolute;left:434px;top:762px;width:142px;height:88px;border:2px solid #222;background:linear-gradient(160deg,#c5c3c1,#9e9a97 55%,#2a2a2c)}
.video-bar{position:absolute;left:0;right:0;bottom:0;height:9px;background:#1b1b1b}
.video-bar span{position:absolute;top:4px;left:24px;width:90px;height:1px;background:#888}

/* footer */
.footer-text{position:absolute;left:256px;width:198px;top:1158px;text-align:center;font-family:"Arimo",sans-serif;font-size:5.5px;letter-spacing:.8px;color:#222}
</style>
</head>
<body>

<header class="hero">
  <div class="hero-portrait" role="img" aria-label="Smiling businessman in glasses and suit giving a thumbs up"></div>
  <div class="grid-lines"></div>

  <div class="tile tile-services">
    <div class="label">SERVICES</div>
    <div class="hours">24/7</div>
    <div class="phone">1-555-010-4477</div>
  </div>
  <div class="tile tile-phone-photo" role="img" aria-label="Black rotary telephone on blue background"></div>

  <div class="tile tile-brand">
    <span class="brand-dot"></span>
    <span class="brand-name">Bright Lane<br>Collective</span>
  </div>

  <a class="nav" style="left:345.6px" href="#">
    <svg viewBox="0 0 16 16"><path d="M8 1 0 8h2v7h4.5v-4.5h3V15H14V8h2z"/></svg>HOME</a>
  <a class="nav" style="left:460.8px" href="#">
    <svg viewBox="0 0 16 16"><ellipse cx="9" cy="6" rx="7" ry="5"/><path d="M3 9 1 14l6-3z"/></svg>ABOUT US</a>
  <a class="nav" style="left:576px" href="#">
    <svg viewBox="0 0 16 16"><circle cx="12" cy="3" r="2.5"/><circle cx="3" cy="8" r="2.5"/><circle cx="12" cy="13" r="2.5"/><path d="M3 8 12 3M3 8l9 5" stroke="#111" stroke-width="1.5"/></svg>NETWORK</a>

  <div class="tile tile-painting"><div class="big">PAINTING</div><div class="small">CONSULTANT</div></div>
  <div class="tile tile-car" role="img" aria-label="Front of a dark car with licence plate"></div>
  <div class="tile tile-tools" role="img" aria-label="Hammer, nails and tools on wooden boards"></div>
  <div class="tile tile-paint" role="img" aria-label="Dripping yellow and orange paint"></div>
  <div class="tile tile-auto">AUTOMOTIVE</div>
  <div class="hero-fade"></div>
</header>

<!-- about -->
<section class="about">
  <div class="rule" style="left:231px;top:461px;width:77px"></div>
  <div class="rule" style="left:345px;top:461px;width:83px"></div>
  <svg class="abs" style="left:315px;top:438px" width="22" height="26" viewBox="0 0 22 26" aria-hidden="true">
    <circle cx="11" cy="5" r="5" fill="#e0661a"/>
    <path d="M0 26V15q0-4 5-4h12q5 0 5 4v11z" fill="#e0661a"/>
    <path d="M11 12l-2 3 2 7 2-7z" fill="#fff"/>
  </svg>
  <h2 class="section-title" style="left:0;width:656px;text-align:center;top:477px;font-size:22px">ABOUT US</h2>

  <div class="bracket-tl" style="left:116px;top:534px"></div>
  <div class="photo" style="left:120px;top:556px;width:92px;height:62px;background:radial-gradient(ellipse at 50% 55%,#2b2b2b 0 45%,#f1f0f1 70%)" role="img" aria-label="Black rotary telephone"></div>
  <div class="bracket-br" style="left:203px;top:623px"></div>

  <h3 class="kicker" style="left:226px;top:532px;font-size:13px">LANE COLLECTIVE</h3>
  <p class="body-copy" style="left:229px;top:567px;width:376px">The founders of Bright Lane Collective have over 30 years in the St. Louis automotive and HVAC industries. In both markets, among many others, one thing is dear: A consumer gets better service at a lower price when they know who to call.  Opening up a phonebook, newspaper, or randomly selected online business could cost you hundreds, even thousands of dollars too much money.  Sometimes all you really need is a Bright Lane.</p>
  <a class="read-more" style="left:555px;top:636px" href="#">READ MORE</a>
</section>

<!-- network -->
<section class="network">
  <div class="rule" style="left:284px;top:666px;width:146px"></div>
  <div class="rule" style="left:76px;top:702px;width:148px"></div>
  <div class="rule" style="left:510px;top:702px;width:104px"></div>
  <svg class="abs" style="left:281px;top:677px" width="36" height="36" viewBox="0 0 36 36" aria-hidden="true">
    <circle cx="18" cy="18" r="18" fill="#e0661a"/>
    <path d="M18 10 11 23h14z" stroke="#fff" stroke-width="1.5" fill="none"/>
    <circle cx="18" cy="10" r="3.2" fill="#fff"/><circle cx="11" cy="23" r="3.2" fill="#fff"/><circle cx="25" cy="23" r="3.2" fill="#fff"/>
  </svg>
  <h2 class="section-title" style="left:327px;top:681px;font-size:22px"><span style="font-size:14px;color:#1a1a1a">OUR</span> NETWORK</h2>

  <h3 class="col-title" style="left:182px;top:737px">OUR NETWORK</h3>
  <svg class="abs" style="left:127px;top:772px" width="38" height="36" viewBox="0 0 38 36" aria-hidden="true" fill="none" stroke="#111" stroke-width="5" stroke-linecap="round">
    <path d="M16 12l6-6a6 6 0 0 1 9 9l-6 6"/><path d="M22 24l-6 6a6 6 0 0 1-9-9l6-6"/><path d="M14 22l10-10" stroke-width="3"/>
  </svg>
  <ul class="service-list" style="left:182px;top:772px">
    <li>Heating.</li><li>Air Conditioning</li><li>Automotive Maintenance</li><li>Automotive Sales</li>
  </ul>
  <ul class="service-list" style="left:305px;top:772px">
    <li>Home Repair.</li><li>Carpentry</li><li>Painting</li><li>Chiropractic.</li>
  </ul>
  <p class="note" style="left:183px;top:822px"><strong>Don't</strong> see what you need, let us know.<br>We will find you the best in the business!!</p>

  <div class="abs" style="left:400px;top:752px;width:1px;height:96px;background:#666"></div>

  <h3 class="col-title" style="left:432px;top:738px">TO KNOW ABOUT US</h3>
  <div class="video" role="img" aria-label="Video still of the smiling businessman giving a thumbs up">
    <div class="video-bar"><span></span></div>
  </div>

  <div class="rule" style="left:76px;top:871px;width:538px;background:#555"></div>
</section>

<!-- vision -->
<section class="vision">
  <svg class="abs" style="left:262px;top:886px" width="28" height="28" viewBox="0 0 28 28" aria-hidden="true">
    <circle cx="14" cy="14" r="13" fill="none" stroke="#e0661a" stroke-width="1.8"/>
    <rect x="7" y="13" width="11" height="7" fill="#e0661a"/>
    <circle cx="10" cy="10" r="2.6" fill="#e0661a"/><circle cx="15.5" cy="10" r="2.6" fill="#e0661a"/>
    <path d="M18 16l4-3v7l-4-3z" fill="#e0661a"/>
  </svg>
  <h2 class="section-title" style="left:310px;top:886px;font-size:22px">OUR VISION</h2>
  <div class="rule" style="left:260px;top:925px;width:146px"></div>

  <div class="bracket-tl" style="left:129px;top:972px"></div>
  <div class="photo" style="left:134px;top:976px;width:95px;height:94px;background:linear-gradient(160deg,#6b4a1e,#c88a2e 45%,#2d2a22)" role="img" aria-label="Child in a red hat and dark coat outdoors in autumn"></div>
  <div class="bracket-br" style="left:214px;top:1057px"></div>

  <h3 class="kicker" style="left:239px;top:971px;font-size:9.3px">SHARING THEIR INDUSTRY CONNECTIONS WITH EVERYONE</h3>
  <p class="body-copy" style="left:239px;top:1002px;width:372px">Bright Lane Collective is now sharing their industry connections with everyone.  It's no longer necessary to have a friend or family member in the business to get the service and prices you deserve.  Bright Lane Collective, connecting YOU with the most reputable and affordable businesses in Saint Louis.</p>
  <a class="read-more" style="left:566px;top:1070px" href="#">READ MORE</a>
</section>

<footer>
  <div class="rule" style="left:256px;top:1152px;width:198px;background:#333"></div>
  <p class="footer-text">ALL COPYRIGHTS RESEVED BY HARLOW STUDIO</p>
  <div class="rule" style="left:256px;top:1171px;width:198px;background:var(--orange)"></div>
</footer>

</body>
</html>
```